Design for Cards used in Corporate Leadership and Communications Card Game

Background:
Steadfast Cornerworks is an organizational development consulting firm that helps organizations improve leadership, communications, and team work through simple and easy methods. We believe that the systems and methods commonly used in companies are overly complex and contrary to what people do intuitively. Our methods work with what people do naturally and innately. Our brand conveys simplicity and ease of use. We often use just black and white with a touch of color in our look and feel along with Zen imagery. Our tag line is "Quiet steps, lasting gains."
Purpose of project:
This project is a card game used in corporate settings to improve leadership and communications skills. The cards portray a successful leader with their bios, values, and behaviors.
The cards are 4 by 6 inches, color, and two-sided, with a picture and text on the front and just text on the back. The game is a work in progress so it is important that we can use the design template to create more cards. Our preference is Microsoft Word or Powerpoint. The source files attached are in Word.
Desired look:
The look and feel we want to create is clean, clear, simple, easy to read, and down to earth with a zen feel optional. We would like to have our logo somewhere on the card. They need to appeal to a professional audience.
Summary of requirements:
• 4x6 inch playing cards depicting bios
• Color, double-sided
• Instruction card is all text
• Includes Steadfast Cornerworks logo
• Must be able to edit design template for future use
• Word or Powerpoint template
• Desired look and feel: professional, clear, easy-to-read, down-to-earth, perhaps zen
Files attached:
• 5 cards including instruction card
• Logo image
. Company business card just for reference
Updates

Please note that the business card was included for reference only so you could see our current look and feel. The logo file is Steadfast Cornerworks. Please do not include the business card in your design, just the Steadfast Cornerworks logo.

Target Market(s)

The target market is business and professional managers who desire a creative and fun way to improve the team working and communication skills of their employees.

Industry/Entity Type

Communications

Requirements
Must have
• Must fit in 4X 6 format in either Word or Powerpoint. Must be very easy to read and clean feel.
Nice to have
• Zen feel
Should not have
• Lots of color, modern look, hard to read font

PLEASE NOTE: Business card was included for reference only. Should not be part of design.

```html
<!DOCTYPE html>
<html lang="en">
<head>
<meta charset="utf-8">
<title>Leader Card – Harlan Brace</title>
<link rel="stylesheet" href="https://fonts.googleapis.com/css2?family=Arimo:wght@400;700&display=swap">
<style>
  :root {
    --teal: #17a78b;
    --ink: #111111;
    --paper: #ffffff;
    --photo-dark: #2a2c3a;
    --photo-mid: #7a4a3c;
  }
  * { box-sizing: border-box; margin: 0; padding: 0; }
  html, body {
    width: 798px; height: 1200px; overflow: hidden;
    background: var(--paper);
  }
  .card {
    position: relative; width: 798px; height: 1200px;
    background: var(--paper); color: var(--ink);
    font-family: "Arimo", Arial, sans-serif;
  }
  .brand {
    position: absolute; left: 14px; top: 12px; height: 290px;
    writing-mode: vertical-rl; transform: rotate(180deg);
    font-weight: 700; font-size: 25px; letter-spacing: 0.5px;
    color: var(--ink); text-align: center;
  }
  .hero-band {
    position: absolute; left: 163px; top: 185px;
    width: 494px; height: 247px; background: var(--teal);
  }
  .portrait {
    position: absolute; left: 245px; top: 4px;
    width: 348px; height: 348px; border-radius: 50%;
    border: 9px solid var(--teal);
    background: radial-gradient(circle at 50% 40%, var(--photo-mid) 0%, var(--photo-dark) 70%);
  }
  .leader-name {
    position: absolute; left: 163px; top: 378px; width: 494px;
    display: flex; align-items: center; justify-content: center; gap: 18px;
    color: var(--paper); font-weight: 700; font-size: 41px;
  }
  .leader-name::before, .leader-name::after {
    content: ""; width: 62px; height: 3px; background: var(--paper);
  }
  .section-title {
    position: absolute; left: 0; width: 798px;
    display: flex; align-items: center; gap: 14px;
    color: var(--teal); font-size: 33px; font-weight: 400; line-height: 1;
  }
  .section-title::before, .section-title::after {
    content: ""; flex: 1; height: 3px; background: var(--teal);
    margin-top: 10px;
  }
  .section-text {
    position: absolute; left: 28px; width: 770px;
    font-size: 30px; line-height: 37px; white-space: nowrap;
  }
  .section-text.centered { left: 0; width: 798px; text-align: center; }
  .questions { list-style: none; line-height: 37.5px; }
  .questions li::before { content: "•"; margin-right: 4px; }
</style>
</head>
<body>
<main class="card">
  <div class="brand">Steadfast Cornerworks</div>

  <div class="hero-band"></div>
  <div class="portrait" role="img" aria-label="Portrait photo of the featured leader"></div>
  <h1 class="leader-name">Harlan Brace</h1>

  <h2 class="section-title" style="top:452px">Lesson</h2>
  <p class="section-text centered" style="top:488px">If you do something, do it big.</p>

  <h2 class="section-title" style="top:537px">Bio</h2>
  <p class="section-text" style="top:568px">Real estate developer, author, public figure.&nbsp; Turned his<br>father’s conservative development company into one<br>that developed casinos and high profile residential<br>projects. He also used debt financing to increase<br>profits. His investments in NYC during the city’s near-<br>bankruptcy helped restore the city’s confidence.</p>

  <h2 class="section-title" style="top:791px">Goals</h2>
  <p class="section-text" style="top:825px; line-height:36px">Gain power and fame; elevate visibilty and personal<br>brand; win.</p>

  <h2 class="section-title" style="top:890px">Governing Principle</h2>
  <p class="section-text" style="top:922px">Generate excitement.</p>

  <h2 class="section-title" style="top:955px">Questions</h2>
  <ul class="section-text questions" style="top:993px; left:18px; width:780px">
    <li>How can you make a big splash?</li>
    <li>How does this help your brand?</li>
    <li>How do you grab the spotlight?</li>
    <li>Is this big enough to be worth the effort?</li>
    <li>What opportunities lend themselves to bigger and better?</li>
  </ul>
</main>
</body>
</html>
```